Business Cards For A cell Phone Company
Linden Cellular
Business Cards For A cell Phone Company - Retailers
Creative Brief
Simple
Tobias Krell
Operations Manager
2864 Belmore Ave Cincinnati OH 45219
tobias.krell@lindencellular-mail.com
www.lindencellular-mail.com
Concepts
Business Cards/Letterhead/ Envelopes/Notepads/Tshirt/labels for quiet tin crate
Business cards and company letter head for Orchard Noodle Court

```html
<!DOCTYPE html>
<html lang="en">
<head>
<meta charset="utf-8">
<title>Linden Cellular Business Card</title>
<link rel="stylesheet" href="https://fonts.googleapis.com/css2?family=Open+Sans:wght@400;600;700&display=swap">
<style>
  :root {
    --bg: #e9e7e4;
    --card: #f7f7f7;
    --red: #c4161c;
    --red-deep: #8f0b11;
    --red-light: #e0262e;
    --silver: #b9babd;
    --ink: #ffffff;
    --shadow: rgba(0,0,0,0.18);
  }
  * { margin: 0; padding: 0; box-sizing: border-box; }
  html, body { width: 1200px; height: 901px; overflow: hidden; }
  body {
    background: var(--bg);
    font-family: "Open Sans", Arial, sans-serif;
    position: relative;
  }
  .card {
    position: absolute;
    left: 290px;
    width: 620px;
    height: 354px;
    background: var(--card);
    box-shadow: 0 6px 18px var(--shadow);
    overflow: hidden;
  }
  .card--front { top: 70px; }
  .card--back { top: 477px; }

  .brand {
    position: absolute;
    display: flex;
    align-items: center;
    gap: 18px;
  }
  .brand__dot {
    border-radius: 50%;
    background: var(--red);
    flex: none;
  }
  .brand__name {
    color: var(--red);
    font-weight: 700;
    text-transform: uppercase;
    letter-spacing: 1px;
    line-height: 1;
    white-space: nowrap;
  }
  .card--front .brand { left: 40px; top: 88px; }
  .card--front .brand__dot { width: 170px; height: 170px; }
  .card--front .brand__name { font-size: 34px; margin-left: 50px; }

  .back__art { position: absolute; inset: 0; }
  .card--back .brand { right: 26px; top: 70px; flex-direction: column; gap: 14px; }
  .card--back .brand__dot { width: 70px; height: 70px; }
  .card--back .brand__name { font-size: 22px; text-align: center; }

  .person { position: absolute; left: 28px; top: 42px; color: var(--ink); }
  .person__name { font-size: 20px; font-weight: 700; }
  .person__title { font-size: 13px; font-weight: 400; margin-top: 2px; }

  .contacts {
    position: absolute;
    left: 28px;
    top: 212px;
    list-style: none;
    color: var(--ink);
    font-size: 10.5px;
    line-height: 1.3;
  }
  .contacts li { display: flex; align-items: center; gap: 8px; min-height: 18px; }
  .contacts li.contacts__address { margin-bottom: 4px; }
  .contacts svg { width: 12px; height: 12px; flex: none; }
</style>
</head>
<body>

<section class="card card--front">
  <div class="brand">
    <span class="brand__dot"></span>
    <span class="brand__name">Linden Cellular</span>
  </div>
</section>

<section class="card card--back">
  <svg class="back__art" viewBox="0 0 620 354" width="620" height="354" aria-hidden="true">
    <defs>
      <radialGradient id="redField" cx="0.35" cy="0.4" r="0.75">
        <stop offset="0" stop-color="#e0262e"/>
        <stop offset="1" stop-color="#8f0b11"/>
      </radialGradient>
      <linearGradient id="silverEdge" x1="0" y1="0" x2="0" y2="1">
        <stop offset="0" stop-color="#9c9ea2"/>
        <stop offset="0.5" stop-color="#e6e6e8"/>
        <stop offset="1" stop-color="#9c9ea2"/>
      </linearGradient>
    </defs>
    <path d="M0 0 H402 C 352 50, 318 120, 350 190 C 378 250, 372 310, 350 354 H0 Z" fill="url(#silverEdge)"/>
    <path d="M0 0 H388 C 338 50, 304 120, 336 190 C 364 250, 358 310, 336 354 H0 Z" fill="url(#redField)"/>
  </svg>

  <div class="person">
    <div class="person__name">Tobias Krell</div>
    <div class="person__title">Operations Manager</div>
  </div>

  <ul class="contacts">
    <li class="contacts__address"><svg viewBox="0 0 12 12"><circle cx="6" cy="6" r="6" fill="#fff"/><path d="M6 2.8a2 2 0 0 1 2 2c0 1.5-2 4-2 4s-2-2.5-2-4a2 2 0 0 1 2-2z" fill="#c4161c"/></svg><span>2864 Belmore Ave,<br>Cincinnati OH 45219</span></li>
    <li><svg viewBox="0 0 12 12"><circle cx="6" cy="6" r="6" fill="#fff"/><path d="M4 3h1.4l.6 1.6-.8.6a4 4 0 0 0 1.6 1.6l.6-.8L9 6.6V8H8A5 5 0 0 1 4 4z" fill="#c4161c"/></svg>513-555-0142</li>
    <li><svg viewBox="0 0 12 12"><circle cx="6" cy="6" r="6" fill="#fff"/><path d="M4 3h1.4l.6 1.6-.8.6a4 4 0 0 0 1.6 1.6l.6-.8L9 6.6V8H8A5 5 0 0 1 4 4z" fill="#c4161c"/></svg>513-555-0187</li>
    <li><svg viewBox="0 0 12 12"><circle cx="6" cy="6" r="6" fill="#fff"/><rect x="4.3" y="2.6" width="3.4" height="6.8" rx="0.6" fill="#c4161c"/></svg>513-555-0129</li>
    <li><svg viewBox="0 0 12 12"><circle cx="6" cy="6" r="6" fill="#fff"/><rect x="3" y="4" width="6" height="4.2" fill="#c4161c"/><path d="M3 4l3 2.4L9 4" stroke="#fff" stroke-width="0.6" fill="none"/></svg>tobias.krell@lindencellular-mail.com</li>
    <li><svg viewBox="0 0 12 12"><circle cx="6" cy="6" r="6" fill="#fff"/><circle cx="6" cy="6" r="3" stroke="#c4161c" stroke-width="0.9" fill="none"/><path d="M3 6h6M6 3v6" stroke="#c4161c" stroke-width="0.7"/></svg>www.lindencellular-mail.com</li>
  </ul>

  <div class="brand">
    <span class="brand__dot"></span>
    <span class="brand__name">Linden Cellular</span>
  </div>
</section>

</body>
</html>
```